New business stationairy

I need paper with header and footer and business cards.
I am a Ltd Company and my main field of expertise is QA/QC inspection in the Oil and Gas Industry. I will need all contact detail inserted and a footer with registration number and bank details etc

Business

```html
<!DOCTYPE html>
<html lang="en">
<head>
<meta charset="utf-8">
<title>Halden Inspection Services Ltd – Stationery</title>
<link rel="stylesheet" href="https://fonts.googleapis.com/css2?family=Barlow:wght@300;400;500;600;700&family=Barlow+Condensed:wght@600;700&display=swap">
<style>
  :root {
    --navy: #1f2055;
    --grey-band: #b4b6ba;
    --card-grey: #bcbdc1;
    --ltd-grey: #b3b5bb;
    --stage: #6d6e72;
    --paper: #ffffff;
    --white: #ffffff;
    --shadow: rgba(0,0,0,0.55);
  }
  * { margin: 0; padding: 0; box-sizing: border-box; }
  html, body { width: 1200px; height: 1089px; overflow: hidden; }
  body { background: var(--stage); font-family: "Barlow", Arial, sans-serif; position: relative; }

  /* Letterhead */
  .letterhead {
    position: absolute; left: 431px; top: 34px; width: 723px; height: 1024px;
    background: var(--paper); box-shadow: 8px 8px 6px var(--shadow);
  }
  .letterhead__title {
    position: absolute; left: 56px; top: 33px;
    font-weight: 700; font-size: 30px; line-height: 32px; color: var(--navy);
    letter-spacing: 1.2px; white-space: nowrap;
  }
  .letterhead__contact-band { position: absolute; left: 39px; top: 67px; width: 542px; height: 27px; }
  .letterhead__contact {
    position: absolute; top: 67px; height: 27px; display: flex; align-items: center; gap: 8px;
    color: var(--white); font-weight: 600; font-size: 13px; white-space: nowrap;
  }
  .letterhead__contact--phone { left: 64px; }
  .letterhead__contact--email { left: 199px; }
  .letterhead__address-label {
    position: absolute; left: 0; top: 106px; width: 122px; height: 17px;
    background: var(--grey-band); color: var(--navy); font-weight: 700; font-size: 12px;
    padding-left: 66px; line-height: 17px;
  }
  .letterhead__address {
    position: absolute; left: 66px; top: 128px; list-style: none;
    color: var(--navy); font-size: 11.5px; line-height: 16px;
  }
  .letterhead__footer-band { position: absolute; left: 237px; top: 923px; width: 486px; height: 22px; }
  .letterhead__registration {
    position: absolute; left: 276px; top: 923px; height: 22px; line-height: 22px;
    color: var(--navy); font-size: 12px; font-weight: 500;
  }
  .letterhead__registration strong { font-weight: 700; }
  .letterhead__bank {
    position: absolute; left: 276px; top: 954px; color: var(--navy); font-size: 12px; font-weight: 500;
  }

  /* Business card front */
  .card-front {
    position: absolute; left: 49px; top: 265px; width: 424px; height: 242px;
    background: var(--navy); box-shadow: 8px 8px 6px var(--shadow);
  }
  .card-front__name {
    position: absolute; left: 14px; top: 88px;
    font-family: "Barlow Condensed", "Arial Narrow", sans-serif; font-weight: 700;
    font-size: 48px; line-height: 43px; color: var(--white); letter-spacing: 1px;
  }
  .card-front__ltd { color: var(--ltd-grey); }

  /* Business card back */
  .card-back {
    position: absolute; left: 49px; top: 534px; width: 424px; height: 243px;
    background: var(--card-grey); box-shadow: 8px 8px 6px var(--shadow);
  }
  .card-back__name {
    position: absolute; left: 54px; top: 30px;
    font-family: "Barlow Condensed", "Arial Narrow", sans-serif; font-weight: 700;
    font-size: 21px; line-height: 17px; color: var(--navy);
  }
  .card-back__address {
    position: absolute; right: 32px; top: 71px; list-style: none; text-align: right;
    color: var(--navy); font-weight: 300; font-size: 14px; line-height: 15.5px;
  }
  .card-back__band { position: absolute; left: 0; width: 267px; height: 19px; }
  .card-back__band--email { top: 175px; }
  .card-back__band--phone { top: 200px; }
  .card-back__contact {
    position: absolute; left: 53px; height: 19px; display: flex; align-items: center; gap: 8px;
    color: var(--navy); font-size: 14px; font-weight: 400; white-space: nowrap;
  }
  .card-back__contact--email { top: 175px; }
  .card-back__contact--phone { top: 200px; }
</style>
</head>
<body>

<section class="letterhead" aria-label="Letterhead">
  <h1 class="letterhead__title">HALDEN INSPECTION SERVICES LTD</h1>
  <svg class="letterhead__contact-band" viewBox="0 0 542 27" preserveAspectRatio="none" aria-hidden="true">
    <polygon points="8,0 542,0 530,27 0,27" fill="var(--navy)"/>
  </svg>
  <div class="letterhead__contact letterhead__contact--phone">
    <svg width="8" height="13" viewBox="0 0 8 13" aria-hidden="true"><rect x="0.8" y="0.8" width="6.4" height="11.4" rx="1.2" fill="none" stroke="#fff" stroke-width="1.4"/><rect x="3" y="9.6" width="2" height="1.2" fill="#fff"/></svg>
    <span>07700 900418</span>
  </div>
  <div class="letterhead__contact letterhead__contact--email">
    <svg width="11" height="8" viewBox="0 0 11 8" aria-hidden="true"><rect width="11" height="8" fill="#fff"/><polyline points="0,0 5.5,4.5 11,0" fill="none" stroke="#1f2055" stroke-width="1.2"/></svg>
    <span>office@haldeninspect.co.uk</span>
  </div>

  <div class="letterhead__address-label">Address:</div>
  <ul class="letterhead__address">
    <li>The Willows</li>
    <li>Mill Lane</li>
    <li>Elmsworth</li>
    <li>Upper</li>
    <li>Harrowden</li>
    <li>Shropshire</li>
    <li>SY9 4QL</li>
  </ul>

  <svg class="letterhead__footer-band" viewBox="0 0 486 22" preserveAspectRatio="none" aria-hidden="true">
    <polygon points="0,0 486,0 486,22 10,22" fill="var(--grey-band)"/>
  </svg>
  <p class="letterhead__registration">Company Registration # <strong>4827163</strong></p>
  <p class="letterhead__bank">Bank Information:</p>
</section>

<section class="card-front" aria-label="Business card front">
  <h2 class="card-front__name">HALDEN<br>INSPECTION<br>SERVICES <span class="card-front__ltd">LTD</span></h2>
</section>

<section class="card-back" aria-label="Business card back">
  <h2 class="card-back__name">HALDEN<br>INSPECTION<br>SERVICES LTD</h2>
  <ul class="card-back__address">
    <li>The Willows</li>
    <li>Mill Lane</li>
    <li>Elmsworth</li>
    <li>Upper Harrowden</li>
    <li>Shropshire</li>
    <li>SY9 4QL</li>
  </ul>
  <svg class="card-back__band card-back__band--email" viewBox="0 0 267 19" preserveAspectRatio="none" aria-hidden="true">
    <polygon points="0,0 267,0 257,19 0,19" fill="#fff"/>
  </svg>
  <svg class="card-back__band card-back__band--phone" viewBox="0 0 267 19" preserveAspectRatio="none" aria-hidden="true">
    <polygon points="0,0 267,0 257,19 0,19" fill="#fff"/>
  </svg>
  <div class="card-back__contact card-back__contact--email">
    <svg width="11" height="8" viewBox="0 0 11 8" aria-hidden="true"><rect width="11" height="8" fill="#1f2055"/><polyline points="0,0 5.5,4.5 11,0" fill="none" stroke="#fff" stroke-width="1.2"/></svg>
    <span>office@haldeninspect.co.uk</span>
  </div>
  <div class="card-back__contact card-back__contact--phone">
    <svg width="8" height="13" viewBox="0 0 8 13" aria-hidden="true"><rect x="0.8" y="0.8" width="6.4" height="11.4" rx="1.2" fill="none" stroke="#1f2055" stroke-width="1.4"/><rect x="3" y="9.6" width="2" height="1.2" fill="#1f2055"/></svg>
    <span>07700 900418</span>
  </div>
</section>

</body>
</html>
```